Logo for Real Estate Company
Stationary and Business Cards
Simple
Glen Moravek
Broker
412 N. Calloway
Brennan, TX
moravekhomes@briskmail.example
www.moravekproperties.example

```html
<!DOCTYPE html>
<html lang="en">
<head>
<meta charset="utf-8">
<title>Moravek &amp; Associates Real Estate – Business Card</title>
<link href="https://fonts.googleapis.com/css2?family=Open+Sans:wght@400;600;700&display=swap" rel="stylesheet">
<style>
  :root {
    --page-bg: #ecebe8;
    --brand-blue: #3b8fd8;
    --brand-blue-dark: #2f7cc2;
    --card-white: #ffffff;
    --text-grey: #6a6f76;
    --icon-grey: #7e858d;
  }
  html, body {
    margin: 0;
    width: 1200px;
    height: 902px;
    overflow: hidden;
    background: var(--page-bg);
    font-family: "Open Sans", Arial, sans-serif;
  }
  .card {
    position: absolute;
    left: 100px;
    top: 165px;
    width: 1000px;
    height: 572px;
    background: var(--brand-blue);
    border-radius: 14px;
    overflow: hidden;
    box-shadow: 0 6px 18px rgba(0,0,0,0.18);
  }
  .panel {
    position: absolute;
    left: 0;
    right: 24px;
    background: var(--card-white);
    border-radius: 0 34px 34px 0;
  }
  .panel--upper { top: 24px; height: 234px; }
  .panel--lower { top: 296px; bottom: 24px; }
  .brand {
    position: absolute;
    left: 26px;
    top: 130px;
    display: flex;
    align-items: center;
    gap: 12px;
  }
  .brand__mark {
    width: 24px;
    height: 24px;
    border-radius: 50%;
    background: var(--brand-blue);
    flex: none;
  }
  .brand__name {
    font-weight: 700;
    font-size: 26px;
    line-height: 1.15;
    color: var(--brand-blue-dark);
    white-space: nowrap;
  }
  .brand__line { display: block; }
  .nameplate {
    position: absolute;
    left: 30px;
    top: 266px;
    height: 30px;
    line-height: 24px;
    color: var(--card-white);
    font-size: 18px;
    font-weight: 600;
  }
  .nameplate__role { font-weight: 400; }
  .nameplate__sep { margin: 0 8px; font-weight: 400; }
  .contacts {
    position: absolute;
    left: 30px;
    top: 22px;
    margin: 0;
    padding: 0;
    list-style: none;
    color: var(--text-grey);
    font-size: 14px;
  }
  .contacts li {
    display: flex;
    align-items: center;
    gap: 10px;
    height: 24px;
    white-space: nowrap;
  }
  .contacts .contacts__cont { padding-left: 24px; }
  .contacts svg { width: 14px; height: 14px; flex: none; }
</style>
</head>
<body>
  <div class="card">
    <div class="panel panel--upper">
      <div class="brand">
        <span class="brand__mark"></span>
        <span class="brand__name">
          <span class="brand__line">Moravek &amp; Associates</span>
          <span class="brand__line">Real Estate</span>
        </span>
      </div>
    </div>

    <div class="nameplate">
      Glen Moravek<span class="nameplate__sep">|</span><span class="nameplate__role">Broker</span>
    </div>

    <div class="panel panel--lower">
      <ul class="contacts">
        <li>
          <svg viewBox="0 0 14 14"><circle cx="7" cy="7" r="7" fill="var(--icon-grey)"/><path d="M7 3.2a2.5 2.5 0 0 0-2.5 2.5C4.5 7.6 7 10.6 7 10.6s2.5-3 2.5-4.9A2.5 2.5 0 0 0 7 3.2z" fill="#fff"/></svg>
          412 N. Calloway Brennan
        </li>
        <li class="contacts__cont">, TX 70418</li>
        <li>
          <svg viewBox="0 0 14 14"><circle cx="7" cy="7" r="7" fill="var(--icon-grey)"/><path d="M4.6 3.6l1.3-.2.7 1.8-.8.6c.4.9 1.1 1.6 2 2l.6-.8 1.8.7-.2 1.3c-3 .4-5.8-2.4-5.4-5.4z" fill="#fff"/></svg>
          555-301-4182
        </li>
        <li>
          <svg viewBox="0 0 14 14"><circle cx="7" cy="7" r="7" fill="var(--icon-grey)"/><rect x="4.8" y="3" width="4.4" height="8" rx="0.8" fill="#fff"/></svg>
          555-762-9045
        </li>
        <li>
          <svg viewBox="0 0 14 14"><circle cx="7" cy="7" r="7" fill="var(--icon-grey)"/><rect x="3.5" y="5.5" width="7" height="4" fill="#fff"/><rect x="5" y="3.5" width="4" height="2" fill="#fff"/></svg>
          555-301-7531
        </li>
        <li>
          <svg viewBox="0 0 14 14"><circle cx="7" cy="7" r="7" fill="var(--icon-grey)"/><rect x="3.5" y="4.5" width="7" height="5" fill="#fff"/><path d="M3.5 4.5L7 7.3l3.5-2.8" fill="none" stroke="var(--icon-grey)" stroke-width="0.8"/></svg>
          moravekhomes@briskmail.example
        </li>
        <li>
          <svg viewBox="0 0 14 14"><circle cx="7" cy="7" r="7" fill="var(--icon-grey)"/><circle cx="7" cy="7" r="3.6" fill="none" stroke="#fff" stroke-width="0.9"/><path d="M3.4 7h7.2M7 3.4v7.2" stroke="#fff" stroke-width="0.8"/></svg>
          www.moravekproperties.example
        </li>
      </ul>
    </div>
  </div>
</body>
</html>
```